Commercial and Multifamily informational website

We need a website for our commercial real estate management company. We will manage offices, retail, apartments and others. Here is the brief verbiage: Providing quality commercial and multifamily portfolio management to Landlords, REITs, and financial institutions. 

Industry/Entity Type

Real Estate

Number of Pages Required

2 page

Font styles to use
Sans Serif
Other font styles liked:
• Muli, Garamond

Colors
0555a3
5c5c5c
3176b5
85acd3
474747

Requirements
Must have
• Home page and contact page

```html
<!DOCTYPE html>
<html lang="en">
<head>
<meta charset="utf-8">
<title>Norvale Real Estate Management</title>
<link rel="stylesheet" href="https://fonts.googleapis.com/css2?family=Mulish:wght@400;600;700&family=Libre+Baskerville:wght@400;700&display=swap">
<style>
:root{
  --navy:#062d66;
  --navy-deep:#031c45;
  --brand:#0555a3;
  --brand-mid:#3176b5;
  --brand-soft:#85acd3;
  --grey:#5c5c5c;
  --grey-dark:#474747;
  --light:#f2f2f2;
  --footer:#2b2b2b;
  --footer-base:#1d1d1d;
  --white:#ffffff;
}
*{margin:0;padding:0;box-sizing:border-box}
html,body{width:689px;height:1200px;overflow:hidden;background:var(--white)}
body{position:relative;font-family:'Mulish',sans-serif;color:var(--grey-dark)}
.abs{position:absolute}
.serif{font-family:'Libre Baskerville',serif}

/* top bar */
.topbar{left:0;top:0;width:689px;height:22px;background:var(--navy)}
.topbar .contact{position:absolute;top:4px;font-size:8px;color:var(--white);display:flex;align-items:center;gap:5px}
.topbar .phone{font-size:10px;font-weight:700}
.topbar .dot{width:14px;height:14px;border-radius:50%;background:var(--white);display:inline-block;position:relative}

/* header */
.header{left:0;top:22px;width:689px;height:54px;background:var(--white)}
.brand{left:57px;top:8px;display:flex;align-items:center;gap:8px}
.brand .mark{width:34px;height:34px;background:var(--brand)}
.brand .name{font-size:12px;line-height:12px;font-weight:600;color:var(--brand);letter-spacing:.5px;text-transform:uppercase}
.nav{right:0;top:21px;display:flex;font-size:9px;font-weight:600;color:var(--grey-dark)}
.nav a{color:inherit;text-decoration:none;padding:0 14px;border-right:1px solid #ddd}
.nav a.active{color:var(--brand)}

/* hero */
.hero{left:0;top:76px;width:689px;height:270px;background:linear-gradient(100deg,#5d6f86 0%,#3f7fc0 30%,#2a6fb4 60%,#1e5d9f 100%)}
.hero-caption{left:298px;top:174px;width:336px;height:85px;background:rgba(5,85,163,.75)}
.hero-caption h1{position:absolute;right:17px;top:9px;text-align:right;font-size:12.4px;line-height:18.5px;font-weight:600;color:var(--white);text-transform:uppercase;letter-spacing:.2px;white-space:nowrap}
.btn-quote{left:494px;top:246px;width:118px;height:25px;background:#000;border:1px solid #444;border-radius:3px;color:var(--white);font-size:9.5px;font-weight:700;text-align:center;line-height:23px}
.slider-dots{left:570px;top:287px;display:flex;gap:4px}
.slider-dots span{width:8px;height:8px;border-radius:50%;border:1.2px solid var(--white)}
.slider-dots span.on{background:var(--white)}

/* welcome */
.welcome{left:0;top:346px;width:689px;height:158px;background:linear-gradient(180deg,var(--navy) 0%,var(--navy-deep) 100%)}
.welcome-heading{position:absolute;top:30px;left:0;width:100%;display:flex;justify-content:center;align-items:center;gap:16px}
.welcome-heading h2{font-size:14px;font-weight:400;color:var(--white);white-space:nowrap;letter-spacing:.2px}
.welcome-heading h2 b{font-weight:700}
.welcome-heading .rule{width:50px;height:4px;border-top:1px solid var(--brand-soft);border-bottom:1px solid var(--brand-soft);flex:none}
.welcome p{position:absolute;left:58px;top:66px;width:573px;text-align:center;font-size:7.8px;line-height:15.8px;color:var(--white)}

/* services */
.section-title{width:100%;left:0;text-align:center;font-size:16px;color:var(--grey-dark)}
.section-title b{color:var(--navy)}
.title-rule{left:275px;width:140px;height:1px;background:#ccc}
.services-intro{left:178px;top:574px;width:333px;text-align:center;font-size:7px;line-height:9px;color:#333}
.service{top:604px;width:170px;text-align:center}
.service h3{font-family:'Libre Baskerville',serif;font-weight:400;font-size:12px;color:#222;text-transform:uppercase}
.service.featured h3{color:var(--brand)}
.service .frame{margin:10px auto 0;width:80px;height:79px;border:1px solid #d8d8d8;border-radius:3px;box-shadow:0 1px 3px rgba(0,0,0,.12);padding:7px}
.service .tile{width:64px;height:63px;background:var(--grey);display:flex;align-items:center;justify-content:center}
.service.featured .tile{background:var(--brand)}
.service p{margin-top:12px;font-size:7.7px;line-height:11.7px;color:#333}
.service .more{display:block;margin-top:5px;font-size:7.2px;color:var(--brand-mid);text-decoration:underline}
.col-divider{top:625px;width:1px;height:130px;background:#eee}
.arrow-btn{width:21px;height:21px;border-radius:50%;border:1px solid #555;display:flex;align-items:center;justify-content:center}

/* testimonials */
.testimonials{left:0;top:798px;width:689px;height:212px;background:var(--light)}
.video{left:58px;top:827px;width:265px;height:155px;background:linear-gradient(180deg,#7fb6e8 0%,#b4cfe5 35%,#a9684f 55%,#6f4536 85%,#3c5a2f 100%);border:1px solid #333}
.video-bar{left:58px;top:966px;width:265px;height:16px;background:#1a1a1a}
.testi-title{left:370px;top:823px;font-size:15px;color:var(--grey-dark)}
.testi-title b{color:var(--navy)}
.testi-rule{left:370px;top:849px;width:262px;height:3px;border-top:1px solid #ccc;border-bottom:1px solid #ccc}
.mini-arrow{width:14px;height:14px;border-radius:50%;border:1px solid #555;display:flex;align-items:center;justify-content:center}
.avatar{left:371px;top:869px;width:61px;height:61px;border-radius:50%;border:2.5px solid var(--navy);background:radial-gradient(circle at 50% 40%,#d8c2b0 0%,#9aa9bf 60%,#3d5a86 100%)}
.testi-name{left:360px;top:936px;width:83px;text-align:center;font-size:8px;font-weight:700;color:var(--navy)}
.quote{left:449px;top:874px;width:183px;font-size:7.6px;line-height:13.4px;color:#777;text-align:justify}
.quote-mark{font-family:'Libre Baskerville',serif;font-weight:700;color:#888;font-size:10px}

/* footer */
.footer{left:0;top:1010px;width:689px;height:166px;background:var(--footer)}
.footer h4{position:absolute;top:34px;font-size:8.5px;line-height:10px;font-weight:700;color:var(--white);padding-bottom:4px;border-bottom:1px solid #444}
.footer ul{position:absolute;list-style:none;font-size:7.5px;line-height:10px;color:#ddd}
.footer li{height:18.3px}
.footer li::before{content:"•";color:#888;margin-right:6px;font-size:6px}
.footer .info{position:absolute;font-size:7.5px;line-height:11.5px;color:#ddd}
.map{left:312px;top:1063px;width:138px;height:82px;background:linear-gradient(135deg,#8fc2d8 0%,#e9e2c8 40%,#b9d69d 70%,#8fc2d8 100%);border:1px solid #666}
.footer-brand{left:484px;top:1083px;display:flex;align-items:center;gap:7px}
.footer-brand .mark{width:26px;height:26px;border:1.5px solid #cfcfcf}
.footer-brand .name{font-size:9.5px;line-height:10px;font-weight:600;color:#cfcfcf;text-transform:uppercase;letter-spacing:.5px}
.basebar{left:0;top:1176px;width:689px;height:24px;background:var(--footer-base)}
.basebar .copy{position:absolute;left:59px;top:7px;font-size:7.3px;color:var(--white)}
.social{position:absolute;top:4px;width:16px;height:16px;border-radius:50%;background:var(--white)}
</style>
</head>
<body>

<div class="abs topbar">
  <div class="contact" style="left:403px">
    <span class="dot"></span><span>info@norvalerealty.com</span>
  </div>
  <div class="contact phone" style="left:526px">
    <span class="dot"></span><span>(+010) 555 0142</span>
  </div>
</div>

<header class="abs header">
  <div class="abs brand">
    <span class="mark"></span>
    <span class="name">Norvale<br>Real Estate<br>Management</span>
  </div>
  <nav class="abs nav">
    <a class="active">HOME</a><a>ABOUT US</a><a>SERVICES</a><a style="margin-right:57px">CONTACT US</a>
  </nav>
</header>

<section class="abs hero" role="img" aria-label="Businessman sketching a city skyline of office towers on a glass board"></section>
<div class="abs hero-caption">
  <h1>Providing quality commercial and<br>multifamily portfolio management to<br>landlords, REITs, and financial institutions</h1>
</div>
<div class="abs btn-quote">REQUEST A QUOTE</div>
<div class="abs slider-dots"><span class="on"></span><span></span><span></span><span></span></div>

<section class="abs welcome">
  <div class="welcome-heading">
    <span class="rule"></span>
    <h2 class="serif">WELCOME TO <b>NORVALE REAL ESTATE MANAGEMENT</b></h2>
    <span class="rule"></span>
  </div>
  <p>Lorem Ipsum is simply dummy text of the printing and typesetting industry. Lorem Ipsum has been the industry's standard dummy text ever since the 1500s, when an unknown printer took a galley of type and scrambled it to make a type specimen book. It has survived not only five centuries, but also the leap into electronic typesetting, remaining essentially unchanged. It was popularised in the 1960s with the release of Letraset sheets containing Lorem Ipsum passages, and more recently with desktop publishing software like Aldus PageMaker including versions of Lorem Ipsum.</p>
</section>

<h2 class="abs section-title serif" style="top:533px;font-weight:400">OUR <b>SERVICES</b></h2>
<div class="abs title-rule" style="top:557px"></div>
<p class="abs services-intro">Lorem Ipsum is simply dummy text of the printing and typesetting industry. Lorem Ipsum has been the industry's standard dummy text ever since the 1500s,</p>

<div class="abs arrow-btn" style="left:21px;top:676px"><svg width="6" height="8" viewBox="0 0 6 8"><path d="M5 0 1 4 5 8" fill="none" stroke="#333" stroke-width="1.3"/></svg></div>
<div class="abs arrow-btn" style="left:647px;top:676px"><svg width="6" height="8" viewBox="0 0 6 8"><path d="M1 0 5 4 1 8" fill="none" stroke="#333" stroke-width="1.3"/></svg></div>

<div class="abs col-divider" style="left:244px"></div>
<div class="abs col-divider" style="left:446px"></div>

<div class="abs service" style="left:57px">
  <h3>Offices</h3>
  <div class="frame"><div class="tile">
    <svg width="30" height="24" viewBox="0 0 30 24" fill="#fff"><rect x="2" y="2" width="14" height="20"/><rect x="16" y="12" width="12" height="10"/><g fill="#5c5c5c"><rect x="5" y="5" width="3" height="3"/><rect x="10" y="5" width="3" height="3"/><rect x="5" y="11" width="3" height="3"/><rect x="10" y="11" width="3" height="3"/><rect x="19" y="15" width="6" height="3"/></g></svg>
  </div></div>
  <p>Lorem Ipsum is simply text of<br>the printing and typesetting industry.<br>Lorem Ipsum has bee indust...</p>
  <a class="more">Read More &raquo;</a>
</div>
<div class="abs service featured" style="left:259px">
  <h3>Retail</h3>
  <div class="frame"><div class="tile">
    <svg width="28" height="26" viewBox="0 0 28 26" fill="#fff"><path d="M2 2h24l2 7H0z"/><rect x="3" y="10" width="22" height="14"/><g fill="#0555a3"><rect x="6" y="13" width="8" height="6"/><rect x="17" y="13" width="5" height="11"/></g></svg>
  </div></div>
  <p>Lorem Ipsum is simply text of<br>the printing and typesetting industry.<br>Lorem Ipsum has bee indust...</p>
  <a class="more">Read More &raquo;</a>
</div>
<div class="abs service" style="left:461px">
  <h3>Apartments</h3>
  <div class="frame"><div class="tile">
    <svg width="22" height="28" viewBox="0 0 22 28" fill="#fff"><rect x="1" y="1" width="20" height="26"/><g fill="#5c5c5c"><rect x="4" y="4" width="3" height="3"/><rect x="9.5" y="4" width="3" height="3"/><rect x="15" y="4" width="3" height="3"/><rect x="4" y="10" width="3" height="3"/><rect x="9.5" y="10" width="3" height="3"/><rect x="15" y="10" width="3" height="3"/><rect x="4" y="16" width="3" height="3"/><rect x="15" y="16" width="3" height="3"/><rect x="8.5" y="20" width="5" height="7"/></g></svg>
  </div></div>
  <p>Lorem Ipsum is simply text of<br>the printing and typesetting industry.<br>Lorem Ipsum has bee indust...</p>
  <a class="more">Read More &raquo;</a>
</div>

<section class="abs testimonials"></section>
<div class="abs video" role="img" aria-label="Video still of a modern brick apartment building with balconies against a blue sky"></div>
<svg class="abs" style="left:172px;top:887px" width="30" height="30" viewBox="0 0 30 30"><circle cx="15" cy="15" r="14" fill="rgba(255,255,255,.55)"/><path d="M12 9 21 15 12 21z" fill="#fff"/></svg>
<div class="abs video-bar">
  <svg width="265" height="16" viewBox="0 0 265 16"><rect x="9" y="4" width="2" height="7" fill="#fff"/><rect x="13" y="4" width="2" height="7" fill="#fff"/><rect x="22" y="7" width="188" height="2" fill="#555"/><rect x="22" y="7" width="86" height="2" fill="#c1121f"/><circle cx="108" cy="8" r="3.5" fill="#eee"/><rect x="205" y="4" width="8" height="8" fill="#888"/><rect x="237" y="4" width="22" height="8" rx="4" fill="#333"/><circle cx="241" cy="8" r="4.5" fill="#ddd"/></svg>
</div>

<h2 class="abs testi-title serif" style="font-weight:400">CLIENT <b>TESTIMNIALS</b></h2>
<div class="abs mini-arrow" style="left:602px;top:825px"><svg width="5" height="6" viewBox="0 0 5 6"><path d="M4 0 1 3 4 6" fill="none" stroke="#333"/></svg></div>
<div class="abs mini-arrow" style="left:619px;top:825px;border-color:#9ab"><svg width="5" height="6" viewBox="0 0 5 6"><path d="M1 0 4 3 1 6" fill="none" stroke="#789"/></svg></div>
<div class="abs testi-rule"></div>
<div class="abs avatar" role="img" aria-label="Portrait photo of the client"></div>
<svg class="abs" style="left:428px;top:890px" width="10" height="14" viewBox="0 0 10 14"><path d="M0 0 8 7 0 14" fill="none" stroke="#062d66" stroke-width="2"/></svg>
<div class="abs testi-name serif">EVAN MARSH</div>
<p class="abs quote"><span class="quote-mark">&ldquo;</span> Lorem Ipsum is simply dummy text of the printing and typesetting industry. Lorem Ipsum has been the industry's standard dummy text ever since the 1500s, when an unknown printer took a galley of type and scrambled it to make a type specimy's standard dummy text ever since the 1500s, when an unknown printer took a galley of type and scrambled. <span class="quote-mark">&rdquo;</span></p>

<footer class="abs footer">
  <h4 style="left:59px;width:58px">Quick Links</h4>
  <ul style="left:59px;top:54px">
    <li>Home</li><li>About Us</li><li>Services</li><li>Contact Us</li>
  </ul>
  <h4 style="left:154px;width:118px">Contact Information</h4>
  <div class="info" style="left:154px;top:56px">norvale real estate management<br>24 Lorem ipsum dolor sit amet sed,<br>Calloway Street no-482910</div>
  <div class="info" style="left:154px;top:96px;display:flex;align-items:center;gap:8px">
    <svg width="7" height="8" viewBox="0 0 7 8"><path d="M1 0h2l.5 2-1 1c.5 1 1 1.5 2 2l1-1 1.5.5V7c-3 .5-6.5-3-6-7z" fill="#ccc"/></svg>555-010-2846</div>
  <div class="info" style="left:154px;top:117px;display:flex;align-items:center;gap:8px">
    <svg width="8" height="6" viewBox="0 0 8 6"><rect width="8" height="6" fill="#ccc"/><path d="M0 0 4 3 8 0" fill="none" stroke="#2b2b2b"/></svg>info@norvalerealty.com</div>
  <h4 style="left:313px;width:137px">Location Map</h4>
</footer>
<div class="abs map" role="img" aria-label="Street map showing the office location"></div>
<svg class="abs" style="left:380px;top:1088px" width="8" height="11" viewBox="0 0 8 11"><path d="M4 11C1 6 0 5 0 4a4 4 0 0 1 8 0c0 1-1 2-4 7z" fill="#d62b2b"/></svg>
<div class="abs footer-brand">
  <span class="mark"></span>
  <span class="name">Norvale<br>Real Estate<br>Management</span>
</div>

<div class="abs basebar">
  <span class="copy">&copy; Copyright 2017 · All Rights Reserved norvale real estate management</span>
  <span class="social" style="left:524px"></span>
  <span class="social" style="left:544px"></span>
  <span class="social" style="left:563px"></span>
  <span class="social" style="left:583px"></span>
</div>

</body>
</html>
```